Complete Re-Design of brettolwin.com

We are looking for a designer/developer that can create a personal branding website design for BrettOlwin.com. The current site is live and operational, but needs a complete redesign to make it more modern, professional, stunning, and to really showcase Brett and his expertise.
We need all the same content and services currently on the site to be migrated over, so keep that in mind when designing the homepage. We want layout, colors, style, and features that will really impress visitors and keep them engaged on the website and ultimately to purchase our services. Ultimately our goal is to gain clients and customers, and to make brett stand out as a trusted expert in his field.
Brett is a domain expert, public speaker, mentor, and coach, a serial entrepreneur and owner of multiple successful online businesses. Please read and review BrettOlwin.com to get a good idea of his background, personality, and what he offers.
An example of a personal branding site that we are impressed with is www.paulvantree.com, however we do NOT necessarily want to copy his site, just use it as a reference for the level of quality we are looking for. We want lots of ideas and options, you as the designer may have unique and innovative ideas that we havent thought of yet that will blow us away. We want to see your creativity in action.
Number of Pages Required
1 page
Requirements
Must have
- https://www.filecrate.net/sh/qk527ravzpew83hn/BBpxTmLKqsRw7GzVbdLMcYNe?oref=e
- file crate link to photos of Brett you can use.
- Must include the current features and options on our current navigation menu, but they can be featured and showcased in a different better way
- This is for an public figure/expert/entreprenuer who is looking to take his personal brand to the next level, and also redesign his website to reflect that.
- We already have a lot of content and images, and videos from his previous site that would need to be transferred over.
Should not have
- Old outdated colors, fonts, images, style. Nothing too feminine.

```html
<!DOCTYPE html>
<html lang="en">
<head>
<meta charset="utf-8">
<title>Brett Olwin – Domain Expert</title>
<link rel="stylesheet" href="https://fonts.googleapis.com/css2?family=Raleway:wght@400;500;600;700&family=Open+Sans:wght@400;600&display=swap">
<style>
:root{
  --navy:#14235e;
  --navy-deep:#0f1d4a;
  --orange:#fd6a17;
  --orange-text:#f27a1e;
  --pale:#eef7fb;
  --ink:#333a44;
  --muted:#5a6068;
  --band:#ececec;
  --white:#ffffff;
}
*{margin:0;padding:0;box-sizing:border-box}
html,body{width:1200px;height:2174px;overflow:hidden}
body{position:relative;background:var(--white);font-family:"Open Sans",Arial,sans-serif;color:var(--ink)}
.abs{position:absolute}
h1,h2,h3,.nav a,.btn{font-family:"Raleway",Arial,sans-serif}
a{text-decoration:none;color:inherit}

/* hero */
.hero{left:0;top:0;width:1200px;height:548px;overflow:hidden}
.hero-photo{left:0;top:0;width:1200px;height:548px;background:linear-gradient(100deg,#f3f5f6 0%,#e7eaec 40%,#d9d4d8 65%,#c9c2c9 80%,#e3e4e6 100%)}
.hero-panel{left:0;top:0;width:371px;height:548px;background:var(--pale);opacity:.92}
.brand{left:210px;top:32px;display:flex;align-items:center;gap:8px;font-family:"Raleway",sans-serif;font-weight:700;font-size:22px;color:var(--navy)}
.brand-mark{width:12px;height:12px;background:var(--orange)}
.nav{left:523px;top:42px;display:flex;gap:38px}
.nav a{font-size:15px;font-weight:500;color:var(--navy)}
.hero-title{left:215px;top:212px;font-size:36px;font-weight:700;color:var(--navy)}
.hero-sub{left:215px;top:262px;font-size:29px;font-weight:700;color:var(--orange-text)}
.hero-text{left:215px;top:311px;width:400px;font-size:11px;line-height:17px;color:var(--muted)}
.btn-outline{left:215px;top:375px;width:118px;height:37px;border:2px solid var(--navy);border-radius:3px;display:flex;align-items:center;justify-content:center;font-size:14px;font-weight:500;color:var(--navy);background:var(--white)}
.dots{left:215px;top:427px;display:flex;gap:5px}
.dots span{width:13px;height:13px;border-radius:50%;background:#b8c1d6}
.dots span:first-child{background:var(--navy)}

/* partners */
.partners{left:0;top:548px;width:1200px;height:81px;background:linear-gradient(#fbfbfb,#e6e6e6);border-top:1px solid #d5d5d5;border-bottom:1px solid #d5d5d5}
.partner{top:28px;font-family:"Raleway",sans-serif;font-weight:700;font-size:21px;color:#8a8d91;transform:translateX(-50%)}

/* about */
.about-photo{left:0;top:629px;width:523px;height:371px;background:linear-gradient(120deg,#6b5a4c 0%,#9a8d80 35%,#c9c9c9 60%,#e6e6e6 100%)}
.about-title{left:545px;top:694px;font-size:30px;font-weight:500;color:var(--navy)}
.about-title span{color:var(--orange-text)}
.about-text{left:545px;top:743px;width:492px;font-size:10.5px;line-height:16.5px;color:var(--muted)}
.about-text p+p{margin-top:10px}
.btn-solid{left:545px;top:878px;width:109px;height:33px;background:var(--navy);border-radius:3px;color:var(--white);font-size:12px;font-weight:600;display:flex;align-items:center;justify-content:center;letter-spacing:.3px}

/* services */
.services{left:0;top:1000px;width:1200px;height:400px;background:var(--orange)}
.services-title{left:0;width:1200px;top:1037px;text-align:center;font-size:28px;font-weight:400;color:var(--white)}
.service{top:1112px;width:180px;transform:translateX(-50%);text-align:center;color:var(--white)}
.service-icon{width:100px;height:100px;margin:0 auto;border:2px solid var(--white);border-radius:50%;display:flex;align-items:center;justify-content:center}
.service h3{margin-top:15px;font-size:16px;font-weight:600}
.service p{margin-top:3px;font-size:9.5px;line-height:14.5px;padding:0 12px}
.service .btn-small{display:inline-block;margin-top:10px;width:80px;height:26px;line-height:23px;border:1.5px solid var(--white);font-family:"Raleway",sans-serif;font-size:11px;font-weight:600}

/* video */
.video{left:0;top:1400px;width:1200px;height:350px;background:radial-gradient(ellipse at 60% 50%,#1d3373 0%,#122458 50%,#0b1a44 100%)}
.video-title{left:0;width:1200px;top:1461px;text-align:center;font-size:28px;font-weight:400;color:var(--white)}
.video-sub{left:0;width:1200px;top:1505px;text-align:center;font-size:16px;font-weight:400;color:#e3e7f2}
.play{left:548px;top:1558px}

/* news */
.news-title{left:212px;top:1803px;font-size:27px;font-weight:400;color:#222}
.news-item{top:1860px;display:flex;gap:17px;width:390px}
.news-thumb{flex:none;width:113px;height:113px;border-radius:4px;background:radial-gradient(circle at 50% 45%,#b8873a 0%,#6e4a1e 45%,#1c1f2b 100%)}
.news-item h3{font-family:"Open Sans",sans-serif;font-size:14.5px;font-weight:400;color:#222;margin-top:-3px}
.news-item p{font-size:9.5px;line-height:14.5px;color:var(--muted);margin-top:6px}

/* footer */
.footer{left:0;top:2050px;width:1200px;height:124px;background:var(--band)}
.footer-nav{left:215px;top:2094px;display:flex;gap:34px;font-family:"Raleway",sans-serif;font-size:14px;font-weight:500;color:#222}
.copyright{left:215px;top:2124px;font-size:10.5px;color:#444}
.social{left:830px;top:2092px;display:flex;gap:14px;font-family:"Raleway",sans-serif;font-size:13px;font-weight:600;color:#555}
</style>
</head>
<body>

<header class="abs hero">
  <div class="abs hero-photo" role="img" aria-label="Portrait photo of Brett Olwin smiling in a bright room with window shutters"></div>
  <div class="abs hero-panel"></div>
  <a class="abs brand" href="#"><span class="brand-mark"></span>Brett Olwin</a>
  <nav class="abs nav">
    <a href="#">About</a><a href="#">Blog</a><a href="#">News</a><a href="#">Services</a><a href="#">Resources</a><a href="#">Press</a>
  </nav>
  <h1 class="abs hero-title">Domain Broker Course</h1>
  <h2 class="abs hero-sub">and Web design Expert</h2>
  <p class="abs hero-text">Eget tempor cursus neque mi consectetuer mi a ultricies massa est sed nisl Class aptent taciti sociosqu ad litora torquent per conubia nostra per inceptos hymenaeos Proin nulla arcu nonummy luctus dictum eget fermentum</p>
  <a class="abs btn btn-outline" href="#">Learn More</a>
  <div class="abs dots"><span></span><span></span><span></span><span></span></div>
</header>

<section class="abs partners" aria-label="Partners">
  <span class="abs partner" style="left:266px">Stratus</span>
  <span class="abs partner" style="left:378px">Norvale</span>
  <span class="abs partner" style="left:505px">Kestrel</span>
  <span class="abs partner" style="left:638px">Lumora</span>
  <span class="abs partner" style="left:776px">Verdant</span>
  <span class="abs partner" style="left:909px">Halcyon</span>
</section>

<section>
  <div class="abs about-photo" role="img" aria-label="Photo of Brett Olwin working on a laptop at home"></div>
  <h2 class="abs about-title">About Brett <span>Olwin</span></h2>
  <div class="abs about-text">
    <p>Brett is a lifelong entrepreneur who at age 18 received a $100,000 job offer while he was just beginning university. He got online in 1985, right after he got my first Orchard computer and in 1989, he ran a large computer store in Toronto.</p>
    <p>He did this until 1994 when he started his own Internet Service provider. After that Brett was hooked on the Internet. He registered his first domain name in 1996 and Brett is one of a small group of individuals to sell a domain name for seven figures. In 2003 Brett purchased NameTalkHub.com, which is now the most popular domain name forum on the Internet.</p>
  </div>
  <a class="abs btn btn-solid" href="#">READ MORE</a>
</section>

<section>
  <div class="abs services"></div>
  <h2 class="abs services-title">Services Provides</h2>

  <div class="abs service" style="left:297px">
    <div class="service-icon">
      <svg width="34" height="34" viewBox="0 0 34 34" fill="#fff"><ellipse cx="17" cy="7" rx="12" ry="4.5"/><path d="M5 11c0 2.5 5.4 4.5 12 4.5s12-2 12-4.5v5c0 2.5-5.4 4.5-12 4.5S5 18.5 5 16z"/><path d="M5 20c0 2.5 5.4 4.5 12 4.5s12-2 12-4.5v5c0 2.5-5.4 4.5-12 4.5S5 27.5 5 25z"/></svg>
    </div>
    <h3>Domain Expert</h3>
    <p>Brett Olwin is the driving force behind NameTalkHub.com, which is one of the most popular domain name forums on the Internet.</p>
    <a class="btn-small" href="#">Read More</a>
  </div>

  <div class="abs service" style="left:494px">
    <div class="service-icon">
      <svg width="38" height="34" viewBox="0 0 38 34" fill="none" stroke="#fff" stroke-width="3"><path d="M3 3v27h32"/><path d="M8 24l8-9 6 5 10-11"/><path d="M26 8h7v7" stroke-width="2.5"/></svg>
    </div>
    <h3>SEO Specialist</h3>
    <p>Brett Olwin is the driving force behind NameTalkHub.com, which is one of the most popular domain name forums on the Internet.</p>
    <a class="btn-small" href="#">Read More</a>
  </div>

  <div class="abs service" style="left:697px">
    <div class="service-icon">
      <svg width="38" height="34" viewBox="0 0 38 34" fill="#fff"><rect x="2" y="3" width="34" height="22" rx="2"/><rect x="15" y="25" width="8" height="5"/><rect x="10" y="29" width="18" height="3"/></svg>
    </div>
    <h3>Web Design</h3>
    <p>Brett Olwin is the driving force behind NameTalkHub.com, which is one of the most popular domain name forums on the Internet.</p>
    <a class="btn-small" href="#">Read More</a>
  </div>

  <div class="abs service" style="left:901px">
    <div class="service-icon">
      <svg width="38" height="34" viewBox="0 0 38 34" fill="#fff"><circle cx="19" cy="8" r="5"/><circle cx="9" cy="12" r="4"/><circle cx="29" cy="12" r="4"/><path d="M11 30c0-6 3.5-10 8-10s8 4 8 10z"/><path d="M2 28c0-5 3-8 7-8 2 0 3 .5 4 1.5-1.5 2-2.5 4-2.5 6.5z"/><path d="M36 28c0-5-3-8-7-8-2 0-3 .5-4 1.5 1.5 2 2.5 4 2.5 6.5z"/></svg>
    </div>
    <h3>Public Expert</h3>
    <p>Brett Olwin is the driving force behind NameTalkHub.com, which is one of the most popular domain name forums on the Internet.</p>
    <a class="btn-small" href="#">Read More</a>
  </div>
</section>

<section>
  <div class="abs video" role="img" aria-label="Dark blue tinted photo of a person working at a computer monitor"></div>
  <h2 class="abs video-title">Integer congue augue et malesuada iaculis</h2>
  <p class="abs video-sub">Praesent elementum elit at tellus nec ultricies amet porttitor</p>
  <svg class="abs play" width="104" height="104" viewBox="0 0 104 104" aria-label="Play video"><circle cx="52" cy="52" r="50" fill="none" stroke="#fff" stroke-width="3"/><path d="M43 35l24 17-24 17z" fill="#fff"/></svg>
</section>

<section>
  <h2 class="abs news-title">News &amp; Awards</h2>
  <article class="abs news-item" style="left:212px">
    <div class="news-thumb" role="img" aria-label="Award medal graphic for 2014"></div>
    <div>
      <h3>Integer congue augue mal</h3>
      <p>felis at cursus magna nisl nec elit Praesent elementum elit at tellus nec ultricies sit amet porttitor mattis enim In massa libero interdum nec interdum vel blandit sed nulla In ullamcorper est eget tempor cursus neque mi</p>
      <p>consectetuer mi a ultricies massa est sed nisl Class aptent taciti sociosqu ad litora torquent per conubia</p>
    </div>
  </article>
  <article class="abs news-item" style="left:616px">
    <div class="news-thumb" role="img" aria-label="Award medal graphic for 2014"></div>
    <div>
      <h3>Curabitur iaculis tempus</h3>
      <p>felis at cursus magna nisl nec elit Praesent elementum elit at tellus nec ultricies sit amet porttitor mattis enim In massa libero interdum nec interdum vel blandit sed nulla In ullamcorper est eget tempor cursus neque mi</p>
      <p>consectetuer mi a ultricies massa est sed nisl Class aptent taciti sociosqu ad litora torquent per conubia</p>
    </div>
  </article>
</section>

<footer>
  <div class="abs footer"></div>
  <nav class="abs footer-nav">
    <a href="#">About</a><a href="#">Blog</a><a href="#">News</a><a href="#">Services</a><a href="#">Resources</a><a href="#">Press</a><a href="#">Contact</a>
  </nav>
  <p class="abs copyright">© 2015 Company Name &nbsp;All right reserved &nbsp;Term of Use</p>
  <div class="abs social">
    <a href="#">Chirp</a><a href="#">Facet</a><a href="#">LinkUp</a><a href="#">PlusOne</a>
  </div>
</footer>

</body>
</html>
```